ECommerce Site Redesign: overall site and specific pages

We have a website that has been in operation for 6+ years, and it's time for a visual refresh.

Our current website is located at http://trx.example

The only significant functional change will be the movement of the persistent vertical navigation bar from the left side up to a categorized horizontal navigation menu. I've attached a rough mockup of how we want this positioned.

No coding necessary; just PSDs. The attached ROUGH MENU MOCKUP.PSD contains a layer with our logo on white should you wish to include it in your submissions.

Target Market(s)

We are an outdoor retailer focused on the high end of the market. We have a general color scheme on our site which we'd like to keep, but various elements need to be made consistent and more aesthetically pleasing.

Our brand is very important to us, and the site design must reflect our values of high quality and affluence. We cater to outdoor enthusiasts, hikers, back packers, and general high end apparel consumers.

Requirements
Must have
• In order to address the issue of consistency, we require strict design guidelines, including font sizing, element spacing, etc.

We require 7 page design templates for:

1.) overall site template - see http://trx.example for current.
* narrow static header bar (NEW)
* footer (KEEP SAME/SIMILAR)
* background
* body
* mini-cart (collapsed and expanded)
* promotion panel (ad box, rotating featured items)
* horizontal navigation bars (expanded/collapsed, grouped by 7 main categories) - see attached ROUGH MENU MOCKUP and see additional notes.
* recently viewed products

2.) product page (see http://trx.example/270599/frostline_heritage-cowl-true-max-mens.aspx for current)
* product imagery/zoombox
* color, size, quantity selection
* add to cart button
* detail tabs
* In-store Availability info
* info panel near the add to cart box for exceptions including:
- Available to pick up in-store only
- Free shipping for your entire order when you purchase this item
- This item is over-sized; please contact a store directly
* "customers who bought this also bought" panel, grid listing of items

3.) product listings (category, search results, etc.)
* item thumbnails in grid format
* sidebar for refinement options (by supplier, by price, by size, etc.)

4.) generic information/content page (see http://trx.example/t-returns.aspx)

5.) store locations page (see http://trx.example/t-TRX.stores.04.aspx)
* store details
* map
* hours
* contact info
* local links
* contact form

6.) contact us form

7.) checkout (see attached current checkout screen shot)
* cart summary
* checkout steps

Any visual elements benefiting from hover effects will need to have both dimmed and hovered layers in the design.

```html
<!DOCTYPE html>
<html lang="en">
<head>
<meta charset="utf-8">
<title>Trailrex Outfitters – Home</title>
<link href="https://fonts.googleapis.com/css2?family=Open+Sans:wght@400;600;700&family=Roboto+Condensed:wght@400;700&display=swap" rel="stylesheet">
<style>
:root{
  --blue:#1a8ad6;
  --blue-dark:#0e6fb5;
  --blue-light:#3ba6ea;
  --purple:#8a4fb8;
  --purple-btn:#9a52d0;
  --ink:#333;
  --muted:#555;
  --line:#e1e1e1;
  --panel:#f3f3f3;
  --footer:#ededed;
  --star:#f0a000;
  --star-off:#999;
}
*{box-sizing:border-box;margin:0;padding:0}
html,body{width:945px;height:1200px;overflow:hidden}
body{position:relative;background:#fff;font-family:"Open Sans",sans-serif;color:var(--ink)}
.abs{position:absolute}
.mountain-band{left:0;top:0;width:945px;height:200px;background:linear-gradient(180deg,#9fb6cc 0%,#d9e3ec 45%,#eef2f6 100%)}
.page{left:40px;top:35px;width:870px;height:932px;background:#fff}
.logo-name{left:58px;top:52px;font-weight:700;font-size:28px;color:var(--purple);letter-spacing:1px}
.top-links{left:531px;top:52px;font-size:11px;color:var(--muted)}
.mini-cart{left:775px;top:48px;width:123px;height:63px;background:linear-gradient(#4a4a4a,#262626);border-radius:2px;color:#fff}
.mini-cart .totals{position:absolute;left:10px;top:8px;font-size:9px;line-height:14px;font-weight:600}
.mini-cart svg{position:absolute;right:10px;top:7px}
.mini-cart .links{position:absolute;left:0;bottom:0;width:100%;height:20px;background:#1c1c1c;font-size:9.5px;text-align:center;line-height:20px;font-weight:600}
.mini-cart .links span{color:#5cb8f5}
.nav-bar{left:10px;top:113px;width:928px;height:47px;background:linear-gradient(var(--blue-light),var(--blue) 50%,var(--blue-dark));border:2px solid #5fbdf5;box-shadow:0 2px 3px rgba(0,0,0,.25)}
.nav{left:56px;top:124px;display:flex;font-family:"Roboto Condensed",sans-serif;font-size:15px;color:#fff}
.nav li{list-style:none;height:26px;line-height:26px;padding:0 10px;margin-right:22px}
.nav li.active{background:rgba(255,255,255,.12);border:1px solid rgba(255,255,255,.35);border-radius:2px;box-shadow:inset 0 1px 2px rgba(0,0,0,.25)}
.search{left:752px;top:126px;width:143px;height:23px;border:1px solid #63c0f4;background:rgba(255,255,255,.12);color:#fff;font-size:11px;line-height:21px;padding-left:8px}
.search svg{position:absolute;right:7px;top:5px}
.hero{left:48px;top:196px;width:852px;height:280px;border-radius:5px;border:2px solid #c9d4de;background:linear-gradient(160deg,#2f5f9d 0%,#6b8fbf 40%,#e6edf4 70%,#ffffff 100%)}
.dots{left:425px;top:451px;display:flex;gap:7px}
.dots i{display:block;width:11px;height:11px;border-radius:50%;background:#aab3bb}
.dots i.on{background:var(--purple-btn)}
.side-panel{left:48px;width:182px;background:var(--panel);border:1px solid #e0e0e0;border-radius:3px}
.tab{left:40px;height:29px;background:linear-gradient(var(--blue-light),var(--blue-dark));color:#fff;font-family:"Roboto Condensed",sans-serif;font-size:16px;line-height:29px;padding-left:16px;border-radius:3px 3px 0 0}
.tab::after{content:"";position:absolute;left:0;bottom:-8px;border-top:8px solid #0a4f85;border-left:8px solid transparent}
.cat-list{left:48px;top:520px;width:182px;list-style:none;font-size:11.5px;color:#444}
.cat-list li{height:23.7px;line-height:23.7px;padding-left:20px;border-bottom:1px solid #ddd;position:relative}
.cat-list li::before{content:"";position:absolute;left:9px;top:9px;border-left:4px solid #555;border-top:3px solid transparent;border-bottom:3px solid transparent}
.cat-list li.current{color:var(--blue)}
.featured-title{left:58px;top:744px;width:162px;text-align:center;font-size:11px;line-height:14px}
.featured-img{left:61px;top:780px;width:156px;height:105px;background:#fff}
.featured-img .shape{position:absolute;left:55px;top:8px;width:46px;height:88px;border-radius:12px;background:linear-gradient(#4a403c,#2a2220)}
.arrow{top:818px;width:14px;height:26px}
.featured-price{left:48px;top:893px;width:182px;text-align:center;color:var(--blue);font-weight:700;font-size:13.5px}
.products{left:244px;top:490px;width:656px;height:462px;border:2px solid #e4e4e4;border-radius:3px;background:#fff}
.products-head{display:flex;height:36px;border-bottom:1px solid var(--line);background:linear-gradient(#fff,#f3f3f3);font-weight:600;font-size:12.5px;color:#333;align-items:center;white-space:nowrap}
.products-head span{text-align:center}
.row{position:absolute;left:13px;width:626px;height:105px;border-bottom:1px solid var(--line);display:flex;align-items:flex-start}
.thumb{width:119px;height:84px;margin-top:10px;border:1px solid #ddd;box-shadow:0 0 2px rgba(0,0,0,.12);background:#fff;padding:4px;flex:none}
.thumb div{width:100%;height:100%}
.name{width:126px;text-align:center;font-size:11px;line-height:14px;color:#444;padding-top:18px;flex:none}
.brand{display:block;margin-top:12px;font-size:9.5px;font-weight:700;color:#222;letter-spacing:.5px;text-transform:uppercase}
.desc{width:186px;font-size:10px;line-height:14px;color:#333;padding-top:30px;flex:none}
.rating{width:112px;text-align:center;padding-top:34px;flex:none}
.price{font-weight:700;font-size:11.5px;margin-top:14px}
.actions{width:78px;padding-top:30px;margin-left:4px;flex:none}
.btn{display:block;width:74px;height:20px;line-height:20px;text-align:center;font-size:11px;color:#fff;border-radius:2px}
.btn.cart{background:linear-gradient(#b06ae2,var(--purple-btn));border:1px solid #7b3fae}
.btn.details{background:linear-gradient(#555,#2b2b2b);width:56px;margin:8px 0 0 9px}
.footer{left:0;top:967px;width:945px;height:186px;background:var(--footer)}
.fcol{font-size:11.5px;color:#333;line-height:17.5px}
.fcol h4{font-weight:700;font-size:11.5px;margin-bottom:5px}
.fcol ul{list-style:none}
.fcol li{position:relative;padding-left:11px}
.fcol li::before{content:"";position:absolute;left:0;top:7px;border-left:3px solid #666;border-top:2.5px solid transparent;border-bottom:2.5px solid transparent}
.social{font-size:11.5px;line-height:13px;color:#333}
.social .ico{position:absolute;left:0;width:28px;height:28px;border-radius:3px}
.social p{position:absolute;left:36px}
.footer-name{left:745px;top:1112px;width:160px;text-align:center;font-size:14px;font-weight:700;color:#777;letter-spacing:.5px;white-space:nowrap}
.copyright{left:0;top:1168px;width:945px;text-align:center;font-size:11px;color:#333}
</style>
</head>
<body>
<svg width="0" height="0" style="position:absolute"><defs>
<symbol id="star" viewBox="0 0 20 20"><path d="M10 1l2.6 6 6.4.5-4.9 4.2 1.5 6.3L10 14.7 4.4 18l1.5-6.3L1 7.5 7.4 7z"/></symbol>
</defs></svg>

<div class="abs mountain-band" role="img" aria-label="Snowy mountain range under a blue sky"></div>
<div class="abs page"></div>

<header>
  <div class="abs logo-name">Trailrex Outfitters</div>
  <div class="abs top-links">Find a Store &nbsp;/&nbsp; Contact Us &nbsp;/&nbsp; Ph. 888-555-0142</div>
  <div class="abs mini-cart">
    <div class="totals">Items : (0)<br>Total : ($0.00)</div>
    <svg width="30" height="28" viewBox="0 0 30 28" fill="none" stroke="#fff" stroke-width="2"><path d="M9 11L15 3l6 8"/><path d="M2 11h26l-3 14H5z"/><path d="M10 14v8M15 14v8M20 14v8"/></svg>
    <div class="links">View Cart &nbsp;|&nbsp; <span>Checkout</span></div>
  </div>
</header>

<div class="abs nav-bar"></div>
<ul class="abs nav">
  <li class="active">Home</li><li>Women</li><li>Mens</li><li>Gear</li><li>Ultralight</li><li>Inspire</li><li>Reviews</li><li>On Sale</li>
</ul>
<div class="abs search">Search
  <svg width="12" height="12" viewBox="0 0 12 12" fill="none" stroke="#fff" stroke-width="1.8"><circle cx="5" cy="5" r="3.8"/><path d="M8 8l3.2 3.2"/></svg>
</div>

<div class="abs hero" role="img" aria-label="Skiers and a snowboarder racing down a snowy alpine slope"></div>
<div class="abs dots"><i class="on"></i><i></i><i></i><i></i><i></i><i></i></div>

<aside>
  <div class="abs side-panel" style="top:497px;height:193px"></div>
  <div class="abs tab" style="top:490px;width:168px">Category</div>
  <ul class="abs cat-list">
    <li>Sunglasses &nbsp;(13)</li>
    <li class="current">Backpacks &nbsp;(36)</li>
    <li>Hydration &nbsp;(395)</li>
    <li>Tents &amp; Tarps &nbsp;(53)</li>
    <li>Sleeping Bags &nbsp;(88)</li>
    <li>Camp Kitchen &nbsp;(34)</li>
    <li style="border-bottom:0">Ropes &amp; Cordage &nbsp;(98)</li>
  </ul>

  <div class="abs side-panel" style="top:711px;height:207px"></div>
  <div class="abs tab" style="top:704px;width:168px">Today's Featured Items</div>
  <div class="abs featured-title">Cedarpeak Ridgeway Hybrid<br>Jacket - Womens</div>
  <div class="abs featured-img"><div class="shape" role="img" aria-label="Dark hooded women's hybrid jacket"></div></div>
  <svg class="abs arrow" style="left:55px" viewBox="0 0 14 26" fill="none" stroke="#aaa" stroke-width="3"><path d="M12 2L3 13l9 11"/></svg>
  <svg class="abs arrow" style="left:209px" viewBox="0 0 14 26" fill="none" stroke="#aaa" stroke-width="3"><path d="M2 2l9 11-9 11"/></svg>
  <div class="abs featured-price">Price: $379.95</div>
</aside>

<section class="abs products">
  <div class="products-head">
    <span style="width:150px">Products</span>
    <span style="width:112px">Name + Brand</span>
    <span style="width:186px">Description</span>
    <span style="width:110px">Reviews + Price</span>
    <span style="width:94px">Details + Cart</span>
  </div>

  <div class="row" style="top:36px">
    <div class="thumb"><div role="img" aria-label="Red and white women's snowshoe" style="background:linear-gradient(90deg,#f2f2f2,#d9d3cf 40%,#c8483c 55%,#e8e4e0)"></div></div>
    <div class="name">927 Solara<br>White / Coral<span class="brand">Ridgeline</span></div>
    <div class="desc">The ultimate trail walking women's snowshoe, the new Solara 9 Series features Free-Pivot Suspension for natural articulation with</div>
    <div class="rating"><svg width="96" height="16"><g fill="var(--star)"><use href="#star" x="0" width="16" height="16"/><use href="#star" x="20" width="16" height="16"/><use href="#star" x="40" width="16" height="16"/><use href="#star" x="60" width="16" height="16"/></g><use href="#star" x="80" width="16" height="16" fill="var(--star-off)"/></svg><div class="price">Price: $169.00</div></div>
    <div class="actions"><span class="btn cart">Add to Cart</span><span class="btn details">Details</span></div>
  </div>

  <div class="row" style="top:141px">
    <div class="thumb"><div role="img" aria-label="Red ski helmet on grey backdrop" style="background:radial-gradient(circle at 50% 45%,#b3283a 0,#8e1e2c 28%,#5c5c5c 34%,#4a4a4a 100%)"></div></div>
    <div class="name">Drift Brim<br>Helmet<span class="brand">Keenview</span></div>
    <div class="desc">The ultimate trail walking women's snowshoe, the new Solara 9 Series features Free-Pivot Suspension for natural articulation with</div>
    <div class="rating"><svg width="96" height="16"><g fill="var(--star)"><use href="#star" x="0" width="16" height="16"/><use href="#star" x="20" width="16" height="16"/><use href="#star" x="40" width="16" height="16"/></g><g fill="var(--star-off)"><use href="#star" x="60" width="16" height="16"/><use href="#star" x="80" width="16" height="16"/></g></svg><div class="price">Price: $169.95</div></div>
    <div class="actions"><span class="btn cart">Add to Cart</span><span class="btn details">Details</span></div>
  </div>

  <div class="row" style="top:246px">
    <div class="thumb"><div role="img" aria-label="Blue and red avalanche backpack" style="background:radial-gradient(ellipse at 50% 50%,#2d6e9a 0,#1f4e72 45%,#fff 62%)"></div></div>
    <div class="name">Stealth 26L<br>BreathPak<span class="brand">Summit Forge</span></div>
    <div class="desc">The ultimate trail walking women's snowshoe, the new Solara 9 Series features Free-Pivot Suspension for natural articulation with</div>
    <div class="rating"><svg width="96" height="16"><g fill="var(--star)"><use href="#star" x="0" width="16" height="16"/><use href="#star" x="20" width="16" height="16"/><use href="#star" x="40" width="16" height="16"/></g><g fill="var(--star-off)"><use href="#star" x="60" width="16" height="16"/><use href="#star" x="80" width="16" height="16"/></g></svg><div class="price">Price: $245.00</div></div>
    <div class="actions"><span class="btn cart">Add to Cart</span><span class="btn details">Details</span></div>
  </div>

  <div class="row" style="top:351px;border-bottom:0">
    <div class="thumb"><div role="img" aria-label="Black rooftop cargo box" style="background:radial-gradient(ellipse at 50% 40%,#3a3a3a 0,#1c1c1c 40%,#fff 60%)"></div></div>
    <div class="name">Horizon 1600<span class="brand">Roofbay</span></div>
    <div class="desc">The ultimate trail walking women's snowshoe, the new Solara 9 Series features Free-Pivot Suspension for natural articulation with</div>
    <div class="rating"><svg width="96" height="16"><g fill="var(--star)"><use href="#star" x="0" width="16" height="16"/><use href="#star" x="20" width="16" height="16"/><use href="#star" x="40" width="16" height="16"/><use href="#star" x="60" width="16" height="16"/></g><use href="#star" x="80" width="16" height="16" fill="var(--star-off)"/></svg><div class="price">Price: $799.95</div></div>
    <div class="actions"><span class="btn cart">Add to Cart</span><span class="btn details">Details</span></div>
  </div>
</section>

<footer>
  <div class="abs footer"></div>
  <div class="abs fcol" style="left:49px;top:981px">
    <h4>Trailrex Stores</h4>
    <div style="display:flex;gap:12px">
      <ul><li>Abbotsford</li><li>Canmore</li><li>Courtenay</li><li>Medicine Hat</li><li>Nanaimo</li><li>Nelson</li><li>New Denver</li><li>Red Deer</li></ul>
      <ul><li>Revelstoke</li><li>Smithers</li><li>Squamish</li><li>Vancouver</li><li>Victoria/Langford</li></ul>
    </div>
  </div>
  <div class="abs fcol" style="left:326px;top:981px">
    <h4>Site Services</h4>
    <ul><li>Privacy and Security</li><li>Return Policy</li><li>Shipping Rates</li><li>Terms &amp; Conditions</li><li>Site Map</li></ul>
  </div>
  <div class="abs fcol" style="left:535px;top:981px">
    <h4>My TRX</h4>
    <ul><li>My TRX Account Info</li><li>My Address Change</li><li>Recent Order History</li></ul>
    <h4 style="margin-top:12px">About TRX</h4>
    <ul><li>About Us</li><li>Frequently Asked Que</li><li>Contact Us</li></ul>
  </div>
  <div class="abs social" style="left:745px;top:985px;width:180px;height:120px">
    <span class="ico" style="top:0;background:#3b5b98"></span><p style="top:3px">Trailrex Outfitters<br>on Friendbook</p>
    <span class="ico" role="img" aria-label="Portrait of the company president" style="top:39px;background:linear-gradient(#c9a48a,#7a8a9a)"></span><p style="top:42px">Message from our<br>President</p>
    <svg class="ico" style="top:76px" width="28" height="28" viewBox="0 0 28 28" fill="#fff" stroke="#8aa0b0" stroke-width="1.5"><rect x="1" y="6" width="26" height="17"/><path d="M1 6l13 10 13-10" fill="none"/></svg><p style="top:84px">Email our president</p>
  </div>
  <div class="abs footer-name">Trailrex Outfitters</div>
  <div class="abs copyright">© 2012-2013 Trailrex Outfitters Inc. All Rights Reserved</div>
</footer>
</body>
</html>
```